" Seremos uma empresa com foco em REFORMAS e pequenas construçoes. Sou um ex franqueado da empresa Mestre Conserta e mudamos o conceito de reparos para reformas e construçoes como dito acima. "

```html
<!DOCTYPE html>
<html lang="pt-BR">
<head>
<meta charset="utf-8">
<title>Envelope Saco – Obra Leve</title>
<link rel="stylesheet" href="https://fonts.googleapis.com/css2?family=Archivo+Black&family=Archivo:wght@400;700&display=swap">
<style>
  :root {
    --backdrop: #cfcfcf;
    --paper: #ffffff;
    --paper-edge: #e2e2e2;
    --brand-blue: #1f86d6;
    --brand-navy: #0c1a2e;
    --text-light: #ffffff;
  }
  html, body {
    margin: 0;
    width: 1200px;
    height: 1200px;
    overflow: hidden;
    background: var(--backdrop);
  }
  .envelope-sheet {
    display: block;
    width: 1200px;
    height: 1200px;
  }
  .paper { fill: var(--paper); }
  .side-flap { fill: var(--paper); stroke: var(--paper-edge); stroke-width: 1; }
  .top-flap { fill: var(--brand-blue); }
  .footer-band { fill: var(--brand-blue); }
  .brand-mark { fill: var(--brand-blue); }
  .brand-name {
    font-family: "Archivo Black", sans-serif;
    font-size: 74px;
    fill: var(--brand-navy);
  }
  .brand-tagline {
    font-family: "Archivo", sans-serif;
    font-weight: 700;
    font-size: 28px;
    fill: var(--brand-blue);
  }
  .contact-line {
    font-family: "Archivo", sans-serif;
    font-size: 11px;
    fill: var(--text-light);
  }
</style>
</head>
<body>
<svg class="envelope-sheet" viewBox="0 0 1200 1200" xmlns="http://www.w3.org/2000/svg">
  <!-- back panel -->
  <rect class="paper" x="607" y="233" width="521" height="835"/>

  <!-- glue side flap -->
  <polygon class="side-flap" points="96,290 120,260 120,1092 96,1068"/>

  <!-- front panel -->
  <rect class="paper" x="120" y="252" width="487" height="840"/>

  <!-- closing flap -->
  <path class="top-flap" d="M120 252 L132 222 Q136 212 150 212 L578 212 Q590 212 594 222 L607 252 Z"/>

  <!-- brand block -->
  <rect class="brand-mark" x="332" y="590" width="56" height="56"/>
  <text class="brand-name" x="360" y="745" text-anchor="middle">Obra Leve</text>
  <text class="brand-tagline" x="360" y="790" text-anchor="middle">Construções e Reformas</text>

  <!-- footer band with contacts -->
  <rect class="footer-band" x="120" y="955" width="487" height="60"/>
  <text class="contact-line" x="588" y="970" text-anchor="end">Rua das Obras, 120</text>
  <text class="contact-line" x="588" y="983" text-anchor="end">Centro - Cidade/UF - CEP 00000-000</text>
  <text class="contact-line" x="588" y="996" text-anchor="end">(00) 0000-0000 / 0000-0000</text>
  <text class="contact-line" x="588" y="1009" text-anchor="end">www.obraleve.com.br</text>
</svg>
</body>
</html>
```